Real Estate 24"x24" Sign, Business Card, Letter Head and Envelope

This is a 4 project contest. If we choose a design or designs we like from what you sent we are willing to pay an amount at our discretion for that design even if we don't like all your designs for the 4 projects. Please be creative. Attached are our logo files. Please message us with any questions. Thanks and Good Luck!
Project 1: QLTV Realty 24" x 24" yard sign
We want to use the same blue background in our logo for the sign where the logo in white font will be on. CMYK 100,80,0,0. Attached is a sample a local designer made for you to get an idea what we are looking for. In the sample, the website is way too big and the entire sign is very plain and not attractive looking plus blue color is wrong one. We want the logo on top as large as possible but keeping it proportionate and attractive looking buy not too big that it looks odd. The following information can go in white color background or same blue color background color. Our company colors are blue (as per logo), green (as per logo), and white. "Residential & Commercial" goes under the logo. Under that put our phone number "312-948-6051" as large as possible but still looks good and under that our website in much smaller but readable font "www.qltvrealty.com".
Project 2: Envelope
We have two version of the logo. Use one or both. Whatever looks best in your design. The envelope will be white. We only want on top left corner logo and underneath our mailing address: 5197 Larchmere Ave. Skokie, IL 60093-1725. Maybe some creative decorative design at bottom of envelope will look nice
Project 3: Letter Head
We have two version of the logo. Use one or both. Whatever looks best in your design. We want the following information on the top of the letterhead. Logo, address: 5197 Larchmere Ave., Skokie, IL 60093-1725, phone: 312-948-6051, fax: 312-682-9307 website www.qltvrealty.com, email: info@qltvrealty.com
Project 4: Business card
Use either logo. We need cards for two individuals. Information for Person 1: Dev Kulkarni, Managing Broker, Phone: 312-948-6051, Email: dev.kulkarni@qltvrealty.com. Person 2: Ajay Kulkarni Broker Phone: 312-519-8263 Email: ajay.kulkarni@qltvrealty.com. Add Address, Fax and website same as above letter head.

```html
<!DOCTYPE html>
<html lang="en">
<head>
<meta charset="utf-8">
<title>QLTV Realty — Business Card</title>
<link rel="stylesheet" href="https://fonts.googleapis.com/css2?family=Montserrat:wght@400;500;700&display=swap">
<style>
  :root {
    --brand-blue: #123f93;
    --brand-green: #6cb52d;
    --ink: #2a2a2a;
    --paper: #fafafa;
    --backdrop: #e6e6e6;
    --rule: #c9c9c9;
  }
  * { box-sizing: border-box; margin: 0; padding: 0; }
  html, body { width: 1200px; height: 933px; overflow: hidden; }
  body {
    background: var(--backdrop);
    font-family: "Montserrat", sans-serif;
    position: relative;
  }
  .card {
    position: absolute;
    top: 324px;
    width: 490px;
    height: 280px;
  }
  .card--front { left: 69px; background: var(--paper); color: var(--ink); }
  .card--back { left: 647px; background: var(--brand-blue); color: #fff; }

  .brand {
    position: absolute;
    display: flex;
    align-items: center;
    gap: 8px;
    font-weight: 700;
    white-space: nowrap;
  }
  .brand__square { display: block; background: currentColor; }
  .card--front .brand { left: 37px; top: 68px; color: var(--brand-blue); font-size: 26px; }
  .card--front .brand__square { width: 16px; height: 16px; }
  .card--back .brand {
    left: 0; right: 0; top: 98px; justify-content: center;
    font-size: 44px; gap: 14px;
  }
  .card--back .brand__square { width: 26px; height: 26px; }

  .person { position: absolute; right: 36px; top: 118px; text-align: right; }
  .person__name { color: var(--brand-blue); font-weight: 700; font-size: 19px; line-height: 22px; text-transform: uppercase; }
  .person__title { font-size: 13px; line-height: 18px; margin-top: 2px; }

  .divider { position: absolute; left: 37px; right: 36px; top: 171px; border-top: 1px solid var(--rule); }

  .address { position: absolute; left: 37px; top: 218px; font-size: 13.5px; line-height: 18px; font-style: normal; }

  .contacts { position: absolute; right: 36px; top: 184px; list-style: none; font-size: 13.5px; line-height: 18px; }
  .contacts li { display: flex; justify-content: flex-end; align-items: center; gap: 8px; }
  .contacts svg { width: 11px; height: 11px; flex: none; }

  .tagline {
    position: absolute; left: 0; right: 0; top: 212px;
    text-align: center; font-size: 15px; font-weight: 500; letter-spacing: 0.3px;
  }
</style>
</head>
<body>
  <section class="card card--front" aria-label="Business card front">
    <div class="brand"><span class="brand__square"></span>QLTV Realty</div>

    <div class="person">
      <p class="person__name">Dev Kulkarni</p>
      <p class="person__title">Managing Broker</p>
    </div>

    <div class="divider"></div>

    <address class="address">5197 Larchmere Ave.<br>Skokie, IL 60093-1725</address>

    <ul class="contacts">
      <li>312-948-6051
        <svg viewBox="0 0 12 12" aria-hidden="true"><path fill="#123f93" d="M2.4 0.6l2 1.9-1 1.4c0.6 1.5 1.6 2.6 3 3.3l1.4-1 2 1.8-1 2.2C4.9 9.9 1.9 6.9 0.6 1.6z"/></svg>
      </li>
      <li>312-682-9307
        <svg viewBox="0 0 12 12" aria-hidden="true"><g fill="#123f93"><rect x="3" y="0.5" width="6" height="3"/><rect x="0.5" y="4" width="11" height="5" rx="1"/><rect x="3" y="8" width="6" height="3.5"/></g></svg>
      </li>
      <li>dev.kulkarni@qltvrealty.com
        <svg viewBox="0 0 12 12" aria-hidden="true"><g fill="none" stroke="#123f93" stroke-width="1"><rect x="0.8" y="2.2" width="10.4" height="7.6"/><path d="M0.8 2.2L6 6.6l5.2-4.4"/></g></svg>
      </li>
      <li>www.qltvrealty.com
        <svg viewBox="0 0 12 12" aria-hidden="true"><g fill="none" stroke="#123f93" stroke-width="0.9"><circle cx="6" cy="6" r="5.2"/><ellipse cx="6" cy="6" rx="2.3" ry="5.2"/><path d="M0.8 6h10.4M1.7 3.3h8.6M1.7 8.7h8.6"/></g></svg>
      </li>
    </ul>
  </section>

  <section class="card card--back" aria-label="Business card back">
    <div class="brand"><span class="brand__square"></span>QLTV Realty</div>
    <p class="tagline">Residential &amp; Commercial</p>
  </section>
</body>
</html>
```